Website design for an Online pastry shop

Website Name : www.lanternandplum.example

Description of the website and its target audience
We are a premium pastry company producing delicious cakes, macarons, cookies, gelato, and other sweet dessert. Our differentiation is that our products are freshly produced with premium quality imported ingredients and one bite into our products set us apart from other bakery shop. We online retail online so as to provide high quality products at a affordable cost. Our products has received raving reviews by many food enthusiast even the hard to please ones. The products contain more natural ingredients and we do not add preservatives. The return rates for our pastry is almost 80%. You only need to try once to be return customers. Our greatest challenge is getting customer to take the first bite. We are so sure of our products that we are going to give people free food tasting.

We are based in China but all our products are developed by award winning chefs from 5 stars hotel. The target customer is woman 16 to 40+ in china. Working class ladies and demand high quality products. A modern, sophisticated and minimalist website

This is a competitive market and image is crucial for such a food ‘conscious ’ orientated customer. They want to feel that they are buying from a reliable company that take great effort to ensure food cleaniness and safety yet affordable price. We make almost 98% of sub ingredients ourselves and we make it by hand.

Style/theme ideas for the web page design
I am looking for a elegant a little rustic, handmade feel yet sophisticated design - one that is easy to the eye yet functional and easy for the user to navigate through. Good play of fonts to give let it feel unique and customised. Black and white is our corporate colours. However, we do not want black background as it does not tease the taste bud. All our colours should come from our products. Customers should be very close to our products. They eat with their eyes first. Black and white is just accent.

Inspirational and competitors websites
http://www.47tart.example/ ( Key competitor )
I like the simple, clean look. The products are the key focus
https://www.pelvora.example/
clean, fresh and different. Attractive with purpose. Feminine
http://moatandwillow.example/
this has a great layout - lots of information and nicely presented. Very sweet and feminine
http://www.storeharbourly.example/
product features is the focus
http://www.janetobrill.example/store/
fun, feminine, rustic

Number of pages needed : 6 ( Uncoded PSD design only )
Page descriptions
Home Page - This page will show what makes our products stand out from the competitors and provide an introduction of who we are.
2nd page : Product catalogue
3nd page: Detail Product page with pictures and descriptions. Select products size and add to cart....
4rd page: Brand Story with pictures and descriptions.
5th page Contact Us : Here they can contact or schedule an appointment for free product tasting
6th page : Check out page

• Please see the project wire frame file " main page.png " or file number 70

```html
<!DOCTYPE html>
<html lang="en">
<head>
<meta charset="utf-8">
<title>Lantern &amp; Plum — Home</title>
<link href="https://fonts.googleapis.com/css2?family=Lato:wght@300;400;700&family=Great+Vibes&family=Playfair+Display:ital@1&display=swap" rel="stylesheet">
<style>
:root{
  --ink:#1a1a1a;
  --white:#ffffff;
  --mist:#eeeeef;
  --grey:#8a8a8a;
  --grey-dark:#555;
  --line:#cfcfcf;
  --footer:#141414;
  --footer-text:#bdbdbd;
  --accent:#e9692c;
  --box-top:#e6e6e6;
  --box-bottom:#bcbcbc;
}
*{margin:0;padding:0;box-sizing:border-box}
html,body{width:1200px;height:2464px;overflow:hidden}
body{position:relative;background:var(--white);font-family:'Lato',sans-serif;color:var(--ink)}
.abs{position:absolute}

/* header band */
.header-band{left:0;top:0;width:1200px;height:888px;
  background:radial-gradient(ellipse at 6% 45%,#f3d6dc 0,rgba(243,214,220,0) 22%),
             radial-gradient(ellipse at 92% 30%,#f7f7f7 0,rgba(247,247,247,0) 40%),
             linear-gradient(180deg,#ececee 0,#f4f4f5 60%,#f0f0f1 100%)}
.brand-tab{left:452px;top:0;width:296px;height:80px;background:var(--ink);border-radius:0 0 14px 14px;
  display:flex;align-items:center;justify-content:center;gap:14px}
.brand-dot{width:18px;height:18px;border-radius:50%;background:var(--white)}
.brand-name{color:var(--white);font-family:'Lato',sans-serif;font-weight:700;font-size:26px;letter-spacing:1px}
.tagline{left:90px;top:152px;font-size:13px;letter-spacing:1px;color:var(--grey-dark)}
.account{right:130px;top:118px;font-size:13px;letter-spacing:1px;color:var(--grey-dark);word-spacing:6px}
.social{right:130px;top:150px;display:flex;gap:10px}
.social span{width:20px;height:20px;border:2px solid var(--grey-dark);border-radius:3px}
.main-nav{left:90px;top:180px;display:flex;gap:30px;font-size:13px;letter-spacing:1px;color:var(--grey-dark)}
.hero-photo{left:150px;top:280px;width:900px;height:592px;
  background:radial-gradient(ellipse at 40% 45%,#fbf7f0 0,#f1e6d3 30%,#d9c29a 52%,#a58c6e 70%,#5f5547 100%);
  box-shadow:0 2px 8px rgba(0,0,0,.08)}
.hero-arrow{top:560px;width:30px;height:30px}

/* about */
.section-title{left:0;width:1200px;text-align:center;font-size:26px;letter-spacing:3px;font-weight:700;color:#444}
.rule{height:1px;background:var(--line)}
.script{left:0;width:1200px;text-align:center;font-family:'Great Vibes',cursive;font-size:30px;color:#444}
.about-copy{left:0;width:1200px;text-align:center;font-size:15px;line-height:30px;letter-spacing:2px;color:var(--grey-dark);font-weight:700}

/* products */
.product{top:1332px;width:240px}
.product-photo{width:240px;height:196px}
.product-label{display:flex;justify-content:space-between;margin-top:30px;padding:0 16px;
  font-family:'Playfair Display',serif;font-style:italic;font-size:19px;letter-spacing:3px;color:#333}

/* mailing */
.mailing-title{left:266px;top:1680px;font-size:20px;color:#444}
.mailing-field{left:554px;top:1672px;width:284px;height:40px;border:1px solid var(--line);background:var(--white);
  font-size:12px;padding:12px 14px;color:#444}
.mailing-btn{left:844px;top:1672px;width:92px;height:40px;background:var(--accent);color:var(--white);
  font-size:13px;font-weight:700;letter-spacing:1px;text-align:center;line-height:40px}

/* footer */
.site-footer{left:0;top:1804px;width:1200px;height:660px;background:var(--footer)}
.f-head{font-size:14px;letter-spacing:1px;color:#e0e0e0;font-weight:700}
.f-box{width:240px;background:linear-gradient(180deg,var(--box-top),var(--box-bottom));border:1px solid #777;
  font-size:12px;line-height:20px;color:#333;padding:4px 28px 4px 8px}
.f-box::after{content:"";position:absolute;right:4px;top:4px;bottom:4px;width:14px;background:#9a9a9a;border-radius:2px}
.f-text{font-size:13px;line-height:22px;color:var(--footer-text)}
.f-brand{left:940px;top:1836px;width:180px;text-align:center;color:var(--white);font-weight:700;font-size:28px}
.f-brand-dot{width:40px;height:40px;border-radius:50%;border:3px solid var(--white);margin:0 auto 14px}
.f-photo{left:940px;top:1988px;width:180px;height:172px;
  background:radial-gradient(circle at 50% 50%,#2d1f33 0,#3b2740 38%,#d8c49e 44%,#c7b08a 60%,#e6e1dc 100%)}
.f-links{left:0;top:2340px;width:1200px;text-align:center;font-size:13px;color:var(--footer-text);word-spacing:8px}
.f-copy{left:0;top:2390px;width:1200px;text-align:center;font-size:12px;color:#888}
</style>
</head>
<body>

<div class="abs header-band"></div>
<div class="abs brand-tab"><span class="brand-dot"></span><span class="brand-name">Lantern &amp; Plum</span></div>
<div class="abs tagline">FREE DELIVERY FOR ORDERS ABOVE $50</div>
<div class="abs account">LOGIN &nbsp;SIGN UP &nbsp;CART</div>
<div class="abs social"><span></span><span></span><span></span><span></span></div>
<nav class="abs main-nav"><span>CAKES</span><span>MACARONS</span><span>COOKIES</span><span>GELATO</span><span>TASTING ROOM</span><span>ABOUT US</span></nav>

<div class="abs hero-photo" role="img" aria-label="Close-up of a cream cake topped with white chocolate petals on a plate"></div>
<svg class="abs hero-arrow" style="left:30px" viewBox="0 0 30 30"><path d="M19 6 L10 15 L19 24" fill="none" stroke="#fff" stroke-width="3"/></svg>
<svg class="abs hero-arrow" style="left:1140px" viewBox="0 0 30 30"><path d="M11 6 L20 15 L11 24" fill="none" stroke="#fff" stroke-width="3"/></svg>

<h2 class="abs section-title" style="top:944px">ABOUT US</h2>
<div class="abs rule" style="left:430px;top:1000px;width:340px"></div>
<div class="abs script" style="top:1010px">Lorem ipsum dolor sit amet</div>
<p class="abs about-copy" style="top:1074px">WE VALUE FLAVOR OVER FUSS. ARTISAN, HANDCRAFTED AND<br>OTHER GOURMET CONFECTIONS DELIVERED<br>DIRECT TO YOUR DOOR.</p>
<div class="abs rule" style="left:430px;top:1180px;width:340px"></div>

<h2 class="abs section-title" style="top:1232px">FEATURED</h2>
<div class="abs rule" style="left:430px;top:1290px;width:340px"></div>

<div class="abs product" style="left:100px">
  <div class="product-photo" role="img" aria-label="Blueberry cheesecake slice" style="background:linear-gradient(180deg,#f4f4f6 0,#3a2540 40%,#e8d6b2 62%,#f2f2f2 100%)"></div>
  <div class="product-label"><span>CAKES</span><span>$18.00</span></div>
</div>
<div class="abs product" style="left:360px">
  <div class="product-photo" role="img" aria-label="Stack of colourful macarons" style="background:radial-gradient(circle at 30% 40%,#e2813d 0,#7a2a2e 35%,#3f6b3a 65%,#2a1c14 100%)"></div>
  <div class="product-label"><span>MACARONS</span><span>$18.00</span></div>
</div>
<div class="abs product" style="left:620px">
  <div class="product-photo" role="img" aria-label="Chocolate curl cake" style="background:linear-gradient(160deg,#5a3622 0,#2e1a10 50%,#7a4a2e 100%)"></div>
  <div class="product-label"><span>COOKIES</span><span>$18.00</span></div>
</div>
<div class="abs product" style="left:880px">
  <div class="product-photo" role="img" aria-label="Mango mousse cake" style="background:linear-gradient(180deg,#f1eee8 0,#f0a02a 35%,#f6d28a 65%,#dcd3c4 100%)"></div>
  <div class="product-label"><span>GELATO</span><span>$18.00</span></div>
</div>

<div class="abs rule" style="left:180px;top:1640px;width:840px"></div>
<div class="abs mailing-title">Join Our mailing List Box</div>
<div class="abs mailing-field">Email Address</div>
<div class="abs mailing-btn">SUBMIT</div>

<footer class="abs site-footer"></footer>

<div class="abs f-head" style="left:88px;top:1844px">CAKES</div>
<div class="abs f-box" style="left:88px;top:1872px">Mousse Cakes<br>Ice Cream Cakes<br>Mousse Cakes<br>Cheese Cakes</div>
<div class="abs f-head" style="left:88px;top:1986px">MACARONS</div>
<div class="abs f-box" style="left:88px;top:2016px">1st Several Variations of Cookies<br>2nd Several Variations of Cookies<br>3rd Several Variations of Cookies</div>
<div class="abs f-head" style="left:88px;top:2134px">COOKIES</div>
<div class="abs f-box" style="left:88px;top:2162px">Mousse Cakes<br>Ice Cream Cakes<br>Mousse Cakes</div>

<div class="abs f-head" style="left:348px;top:1844px">GELATO</div>
<div class="abs f-box" style="left:348px;top:1872px">Sorbet Cream<br>Sorbet Cream<br>Sorbet Cream</div>
<div class="abs f-head" style="left:348px;top:1986px">QUESTIONS?</div>
<p class="abs f-text" style="left:348px;top:2016px;width:230px">We have developed a variety of characteristic flavors to satisfy your unique taste.</p>
<div class="abs f-head" style="left:348px;top:2134px">PHONE NUMBER</div>
<p class="abs f-text" style="left:348px;top:2164px">+86 555 0142 77<br>Email : info@lanternandplum.example</p>

<div class="abs f-head" style="left:612px;top:1844px">CUSTOMER SERVICE</div>
<div class="abs f-box" style="left:612px;top:1872px">Contact Us<br>Shipping<br>FAQ</div>
<div class="abs f-head" style="left:612px;top:1986px">ABOUT US</div>
<div class="abs f-box" style="left:612px;top:2016px">Our Story, Philosophy Etc.<br>Our Story, Philosophy Etc.<br>Our Story, Philosophy Etc.</div>

<div class="abs f-brand"><div class="f-brand-dot"></div>Lantern &amp; Plum</div>
<div class="abs f-photo" role="img" aria-label="Blueberry cheesecake on a white plate"></div>

<div class="abs rule" style="left:88px;top:2316px;width:1032px;background:#333"></div>
<div class="abs f-links">Cakes | Macarons | Cookies | Gelato | Tasting Room | About Us</div>
<div class="abs f-copy">Copyright 2015 www.lanternandplum.example</div>

</body>
</html>
```